Harbor Wick Candle's Seasonal promotions!

We would like two banners for our website, one for Spring and one for Mothers Day. On the Spring Banner we would like our candles to be featured with a beautiful spring background (flowers, or a garden, etc as long as it's spring)- it does not have to be all of them it could just be one of the four candles I posted, be creative! We would like to include our our Spring deals which is 30% OFF our Spring Collection and free shipping when you purchase $50 or more. Instead of Spring deals put something catchy like "Hello Spring!" or "Spring is here.."
For the mothers day banner we would like a banner with our Evermore candle in it (the large ones with the black label). We leave the creativity to you. We would like to include in this one the deals: 30% OFF and a free 8 ounce air freshener when you purchase $75 dollars or more (a $15 dollar value). As far as wording goes, we would like something pretty and sweet in regards to Mother's Day. We leave the creativity to you. Just note that we want our banners to be elegant and to the point. Please note these banners are separate and the deals are separate.
Updates
Please note: These banners will be on our website, they do not require our logo.Banner size: 314 height x 783 width Added Tuesday, April 14, 2015
Having said that I did upload our logo in case you would like to use it in the banner, it's not necessary but I leave the creativity up to you. Added Tuesday, April 14, 2015

```html
<!DOCTYPE html>
<html lang="en">
<head>
<meta charset="utf-8">
<title>Harbor Wick Candle – Spring Banner Presentation</title>
<link rel="stylesheet" href="https://fonts.googleapis.com/css2?family=Arimo:wght@400;700&family=Satisfy&display=swap">
<style>
  :root {
    --board-light: #f4f4f4;
    --board-dark: #d6d6d6;
    --ink: #111111;
    --ink-soft: #333333;
    --navy-deep: #050c24;
    --navy: #0c2a55;
    --teal: #2fa3b0;
    --teal-glow: #8fe6e8;
    --teal-dark: #1b5f74;
    --title-blue: #1d3c6c;
    --cream: #f6e8d4;
    --forest-deep: #143d10;
    --forest: #2f7a1e;
    --forest-light: #8fd04a;
    --white: #ffffff;
    --icon-blue: #0b2c4a;
    --icon-orange: #3a1f05;
    --icon-red: #3a0a0a;
  }
  * { margin: 0; padding: 0; box-sizing: border-box; }
  html, body { width: 1200px; height: 900px; overflow: hidden; }
  body {
    background: radial-gradient(ellipse at 50% 45%, var(--board-light) 0%, var(--board-dark) 100%);
    font-family: "Arimo", Arial, sans-serif;
    color: var(--ink);
  }
  .board { position: relative; width: 1200px; height: 900px; }
  .board svg { position: absolute; left: 0; top: 0; }

  .label { font-family: "Arimo", Arial, sans-serif; font-size: 22px; letter-spacing: 1px; fill: var(--ink); }
  .dimension-line { stroke: var(--ink); stroke-width: 2; }
  .spec { font-family: "Arimo", Arial, sans-serif; font-size: 12px; fill: var(--ink-soft); }
  .spec-strong { font-weight: 700; fill: var(--ink); }
  .spec-note { font-family: "Arimo", Arial, sans-serif; font-size: 7px; fill: var(--ink-soft); }

  .script { font-family: "Satisfy", cursive; }
  .sans { font-family: "Arimo", Arial, sans-serif; }

  .banner-shadow { filter: drop-shadow(0 3px 5px rgba(0,0,0,0.35)); }

  .spring-night-title { fill: var(--title-blue); font-size: 50px; }
  .spring-night-offer { fill: var(--cream); font-weight: 700; font-size: 36px; }
  .spring-night-on { fill: var(--teal-dark); font-size: 16px; letter-spacing: 1px; }
  .spring-night-collection { fill: var(--title-blue); font-size: 22px; letter-spacing: 3px; }
  .spring-night-free { fill: var(--ink); font-size: 44px; letter-spacing: 6px; }
  .spring-night-ship { fill: var(--ink); font-size: 22px; letter-spacing: 1px; }
  .spring-night-on-small { fill: var(--teal-dark); font-size: 12px; }
  .spring-night-purchase { fill: var(--teal-dark); font-size: 22px; letter-spacing: 1px; }
  .spring-night-amount { fill: #0a2f3e; font-size: 22px; letter-spacing: 1px; }

  .spring-park-title { fill: var(--white); font-size: 52px; }
  .spring-park-candle { fill: var(--white); font-size: 38px; letter-spacing: 6px; }
  .spring-park-offer { fill: var(--white); font-weight: 700; font-size: 38px; }
  .spring-park-on { fill: var(--white); font-size: 18px; }
  .spring-park-collection { fill: var(--white); font-size: 23px; letter-spacing: 3px; }
  .spring-park-shipping { fill: var(--white); font-weight: 700; font-size: 17px; }
</style>
</head>
<body>
<main class="board">
<svg width="1200" height="900" viewBox="0 0 1200 900" xmlns="http://www.w3.org/2000/svg">
  <defs>
    <radialGradient id="night-sky" cx="78%" cy="35%" r="75%">
      <stop offset="0" stop-color="var(--teal-glow)"/>
      <stop offset="0.3" stop-color="var(--teal)"/>
      <stop offset="0.7" stop-color="var(--navy)"/>
      <stop offset="1" stop-color="var(--navy-deep)"/>
    </radialGradient>
    <linearGradient id="product-tones" x1="0" x2="1">
      <stop offset="0" stop-color="#1c1c1c"/>
      <stop offset="1" stop-color="#d9d5ca"/>
    </linearGradient>
    <linearGradient id="blossom-tones" x1="0" y1="0" x2="1" y2="1">
      <stop offset="0" stop-color="#e9f6f7" stop-opacity="0.85"/>
      <stop offset="1" stop-color="var(--teal)" stop-opacity="0.25"/>
    </linearGradient>
    <radialGradient id="park-light" cx="55%" cy="25%" r="80%">
      <stop offset="0" stop-color="#e8f7a8"/>
      <stop offset="0.25" stop-color="var(--forest-light)"/>
      <stop offset="0.65" stop-color="var(--forest)"/>
      <stop offset="1" stop-color="var(--forest-deep)"/>
    </radialGradient>
    <path id="night-arc" d="M 345 245 Q 470 125 612 250"/>
    <path id="park-arc" d="M 158 612 Q 290 468 425 610"/>
  </defs>

  <!-- Width dimension -->
  <g class="dimension">
    <line class="dimension-line" x1="315" y1="73" x2="628" y2="73"/>
    <line class="dimension-line" x1="782" y1="73" x2="1097" y2="73"/>
    <line class="dimension-line" x1="315" y1="60" x2="315" y2="98"/>
    <line class="dimension-line" x1="1097" y1="60" x2="1097" y2="98"/>
    <text class="label" x="705" y="80" text-anchor="middle">783 px</text>
  </g>

  <!-- Height dimension -->
  <g class="dimension">
    <line class="dimension-line" x1="943" y1="498" x2="943" y2="622"/>
    <line class="dimension-line" x1="943" y1="688" x2="943" y2="811"/>
    <line class="dimension-line" x1="920" y1="498" x2="956" y2="498"/>
    <line class="dimension-line" x1="920" y1="811" x2="956" y2="811"/>
    <text class="label" x="946" y="662" text-anchor="middle">314 px</text>
  </g>

  <text class="label" x="153" y="286">Design #1</text>
  <text class="label" x="436" y="854">Design #2</text>

  <!-- Design 1: night teal spring banner -->
  <g class="banner spring-night">
    <rect class="banner-shadow" x="315" y="113" width="783" height="313" fill="url(#night-sky)" role="img" aria-label="Soft dark navy to glowing teal spring backdrop"/>
    <rect x="315" y="113" width="160" height="313" fill="#000" opacity="0.12"/>
    <rect x="1010" y="113" width="88" height="313" fill="#000" opacity="0.12"/>
    <rect x="632" y="182" width="190" height="172" rx="10" fill="url(#product-tones)" opacity="0.9" role="img" aria-label="Photo of the Evermore candle beside its tube and lid"/>
    <rect x="822" y="130" width="275" height="225" rx="40" fill="url(#blossom-tones)" role="img" aria-label="Photo of a white spring blossom on a branch"/>

    <text class="script spring-night-title"><textPath href="#night-arc" startOffset="50%" text-anchor="middle">Harbor Wick</textPath></text>
    <text class="sans spring-night-offer" x="478" y="270" text-anchor="middle">30%</text>
    <text class="sans spring-night-offer" x="478" y="305" text-anchor="middle">OFF</text>
    <text class="sans spring-night-on" x="478" y="345" text-anchor="middle">On</text>
    <text class="sans spring-night-collection" x="478" y="381" text-anchor="middle">Spring Collection</text>

    <text class="sans spring-night-free" x="1002" y="302" text-anchor="middle">Free</text>
    <text class="sans spring-night-ship" x="1000" y="327" text-anchor="middle">shipping</text>
    <text class="sans spring-night-on-small" x="1000" y="351" text-anchor="middle">on</text>
    <text class="sans spring-night-purchase" x="1000" y="381" text-anchor="middle">purchase</text>
    <text class="sans spring-night-amount" x="1000" y="411" text-anchor="middle">$50 or more</text>
  </g>

  <!-- Design 2: sunlit park spring banner -->
  <g class="banner spring-park">
    <rect class="banner-shadow" x="104" y="498" width="783" height="313" fill="url(#park-light)" role="img" aria-label="Photo of a sunlit green park with tall trees and lawn"/>
    <rect x="104" y="498" width="376" height="313" fill="#0d2a08" opacity="0.3"/>
    <rect x="232" y="603" width="140" height="122" rx="10" fill="url(#product-tones)" opacity="0.9" role="img" aria-label="Photo of the Evermore candle beside its tube and lid"/>

    <text class="script spring-park-title"><textPath href="#park-arc" startOffset="50%" text-anchor="middle">Harbor Wick</textPath></text>
    <text class="script spring-park-candle" x="293" y="787" text-anchor="middle">Candle</text>

    <text class="sans spring-park-offer" x="690" y="648" text-anchor="middle">30%</text>
    <text class="sans spring-park-offer" x="690" y="684" text-anchor="middle">OFF</text>
    <text class="sans spring-park-on" x="690" y="713" text-anchor="middle">On</text>
    <text class="sans spring-park-collection" x="690" y="743" text-anchor="middle">Spring Collection</text>
    <text class="sans spring-park-shipping" x="689" y="788" text-anchor="middle">Free shipping on purchase $50 or more</text>
  </g>

  <!-- File specifications -->
  <g class="specs">
    <text class="spec" x="1158" y="755" text-anchor="end"><tspan class="spec-strong" letter-spacing="4">CMYK</tspan> | RGB</text>
    <text class="spec" x="1158" y="783" text-anchor="end">Layered | Resizable</text>
    <text class="spec" x="1160" y="810" text-anchor="end">Transparent <tspan class="spec-strong">PNG</tspan> | <tspan class="spec-strong">JPG</tspan></text>
    <line x1="1022" y1="824" x2="1158" y2="824" stroke="var(--ink-soft)" stroke-width="1"/>
    <rect x="1024" y="838" width="19" height="19" fill="var(--icon-blue)"/>
    <rect x="1082" y="838" width="19" height="19" fill="var(--icon-orange)"/>
    <rect x="1139" y="838" width="19" height="19" fill="var(--icon-red)"/>
    <text class="spec spec-strong" x="1033" y="875" text-anchor="middle">PSD</text>
    <text class="spec spec-strong" x="1091" y="874" text-anchor="middle">EPS | Ai</text>
    <text class="spec spec-strong" x="1148" y="874" text-anchor="middle">PDF</text>
    <text class="spec-note" x="1148" y="884" text-anchor="middle">(Print Ready)</text>
  </g>
</svg>
</main>
</body>
</html>
```